IT Company requires new Business Card design.

Over the years we have had a few different business card designs. We are now due for new cards across the board for all staff. We felt this would be a good time to start fresh with a new design. Our traditional card simply had our details on the front, and a list of services on the back. We don't particularly need the list of services, we have had cards where the only thing on the rear of the card was our logo.
Feel free to be creative, we would like our tag line "Complete IT Management" to appear at some point, doesn't necessarily have to be with the logo.
I have attached samples and drafts of various previous cards we have used over the years.
Industry/Entity Type
Business
Look and feel
Each slider illustrates characteristics of the customer's brand and the style your logo design should communicate.

```html
<!DOCTYPE html>
<html lang="en">
<head>
<meta charset="utf-8">
<title>Complete IT Management – Services Card</title>
<link rel="stylesheet" href="https://fonts.googleapis.com/css2?family=Open+Sans:ital,wght@0,300;0,600;1,400&display=swap">
<style>
  :root {
    --frame: #5f7383;
    --paper: #f3f3f3;
    --heading: #3b3d40;
    --body: #4a4b4d;
  }
  * { margin: 0; padding: 0; box-sizing: border-box; }
  html, body {
    width: 667px;
    height: 1200px;
    overflow: hidden;
    background: var(--frame);
  }
  .card {
    position: relative;
    width: 667px;
    height: 1200px;
    background: var(--frame);
    font-family: "Open Sans", "Segoe UI", sans-serif;
  }
  .card__panel {
    position: absolute;
    left: 14px;
    top: 14px;
    right: 14px;
    bottom: 14px;
    background: var(--paper);
  }
  .card__tagline {
    position: absolute;
    left: 0;
    right: 0;
    top: 131px;
    text-align: center;
    font-size: 29px;
    line-height: 40px;
    font-weight: 600;
    color: var(--heading);
    letter-spacing: 0.2px;
  }
  .service-list {
    position: absolute;
    left: 132px;
    list-style: none;
    font-size: 27px;
    line-height: 37.8px;
    font-weight: 300;
    color: var(--body);
  }
  .service-list--hardware { top: 261px; }
  .service-list--infrastructure { top: 527px; left: 131px; }
  .service-list--online { top: 776px; left: 133px; }
  .card__web {
    position: absolute;
    left: 131px;
    top: 1075px;
    font-size: 27px;
    line-height: 38px;
    font-style: italic;
    font-weight: 400;
    color: var(--heading);
    letter-spacing: 0.6px;
  }
</style>
</head>
<body>
  <main class="card">
    <div class="card__panel">
    </div>
    <h1 class="card__tagline">COMPLETE IT MANAGEMENT</h1>
    <ul class="service-list service-list--hardware">
      <li>Networking</li>
      <li>Servers</li>
      <li>Workstations</li>
      <li>Laptops</li>
      <li>Firewalls</li>
    </ul>
    <ul class="service-list service-list--infrastructure">
      <li>Data Cabling</li>
      <li>All electrical Work</li>
      <li>Server Racks</li>
      <li>Network Infrastructure</li>
      <li>Off site back up</li>
    </ul>
    <ul class="service-list service-list--online">
      <li>ADSL Connections</li>
      <li>Web Hosting</li>
      <li>Web Design</li>
      <li>Website Maintenance</li>
      <li>Domain Names PABX systems</li>
    </ul>
    <p class="card__web">www.harbourlinknet.com.au</p>
  </main>
</body>
</html>
```